BRIGHTPINE RV Resort needs a logo and advertising poster

We need an advertising poster for our epic RV Resort located on north end of Tolvin Lake, (Northern Saskatchewan, trees no mountains)
SEASONAL FULL SERVICE SITES with marina and lake access.
Sauna/plunge, disc golf , hiking/quad trails, and pet friendly.
We are after a fun 70,s themed simple poster. Please use brand guide for colours and redo logo to be Brightpine Resort.

Target Market(s)

RV owners looking for permeant sites. No tenting.

Font styles to use
Other font styles liked:
• See brand guide

Requirements
Must have
• Change exisiting branding to BRIGHTPINE RESORT instead of coffee Emphasis Limited sites.... Referral discount. Phone number.
Nice to have
• .
Should not have
• Keep it simple

```html
<!DOCTYPE html>
<html lang="en">
<head>
<meta charset="utf-8">
<title>Brightpine Resort – Epic Campground</title>
<link rel="stylesheet" href="https://fonts.googleapis.com/css2?family=Titan+One&family=Poppins:wght@500;600&display=swap">
<style>
  :root{
    --cream-bg:#F2DE9E;
    --cream:#F4E4AC;
    --orange:#E0662A;
    --orange-bright:#F28A1E;
    --brown:#4E2412;
    --gold:#D99A2B;
    --teal-text:#9DD0BE;
    --teal-light:#8FC9B5;
    --forest:#1F4A2C;
    --box-fill:#F3E6B5;
    --box-inner:#B9C7B0;
    --white:#FFFFFF;
  }
  *{box-sizing:border-box;margin:0;padding:0}
  html,body{width:1200px;height:1200px;overflow:hidden;background:var(--cream-bg)}
  .poster{position:absolute;left:200px;top:0;width:800px;height:1200px;overflow:hidden;font-family:"Titan One",sans-serif}
  .scene{position:absolute;inset:0;width:100%;height:100%}
  .brand{position:absolute;left:48px;top:58px;display:flex;align-items:center;gap:10px;color:var(--white);font-size:27px;line-height:1.05}
  .brand-mark{width:18px;height:18px;background:var(--white);border-radius:3px;flex:none}
  .headline{position:absolute;left:0;width:100%;text-align:center;color:var(--orange);text-shadow:4px 5px 0 var(--brown);letter-spacing:1px}
  .headline.epic{top:76px;left:0;font-size:90px;line-height:1}
  .headline.camp{top:178px;left:-4px;font-size:84px;line-height:1;transform:rotate(4deg)}
  .subhead{position:absolute;left:0;width:100%;text-align:center;color:var(--cream);text-shadow:3px 3px 0 var(--forest);font-size:38px;line-height:1;transform:rotate(3deg)}
  .subhead.l1{top:270px;left:-4px}
  .subhead.l2{top:305px;left:-4px}
  .tagline{position:absolute;top:360px;left:-4px;width:100%;text-align:center;color:var(--orange);text-shadow:2px 2px 0 var(--cream);font-size:22px;letter-spacing:.3px}
  .badge{position:absolute;left:551px;top:37px;width:218px;height:202px}
  .badge-text{position:absolute;left:551px;top:80px;width:218px;text-align:center;color:var(--orange);font-size:27px;line-height:1.07;letter-spacing:1px}
  .offer{position:absolute;left:0;width:100%;text-align:center}
  .offer.l1{top:843px;left:-6px;font-size:22px;color:var(--cream);text-shadow:2px 2px 0 var(--brown)}
  .offer.l1 .hl{color:var(--teal-light)}
  .offer.l2{top:868px;left:-4px;font-size:40px;color:var(--cream);text-shadow:3px 3px 0 var(--brown)}
  .offer.l2 .hl{color:var(--gold)}
  .amenities{position:absolute;left:48px;top:932px;width:706px;height:124px;background:var(--box-fill);border:7px solid var(--orange);border-radius:28px;box-shadow:inset 0 0 0 5px var(--box-inner)}
  .amenities-title{position:absolute;top:912px;left:0;width:100%;text-align:center;font-size:38px;color:var(--orange-bright);text-shadow:3px 3px 0 var(--brown);z-index:2}
  .amenity-list{list-style:none;position:absolute;inset:0;padding:32px 0 0 24px;display:grid;grid-template-columns:392px 1fr;row-gap:10px}
  .amenity-list li{display:flex;align-items:center;gap:14px;font-size:26px;color:var(--teal-text);text-shadow:2px 2px 0 var(--brown)}
  .amenity-list li::before{content:"";width:24px;height:24px;border-radius:50%;background:var(--orange);border:2px solid var(--brown);flex:none}
  .referral{position:absolute;top:1080px;left:0;width:100%;text-align:center;font-size:36px;color:var(--cream);text-shadow:3px 3px 0 var(--forest);letter-spacing:.5px}
  .contact{position:absolute;left:176px;top:1128px;width:450px;height:42px;border-radius:21px;background:var(--forest);display:flex;align-items:center;justify-content:center;gap:26px;color:var(--cream);font-family:"Poppins",sans-serif;font-weight:600;font-size:21px}
  .contact .phone{display:flex;align-items:center;gap:6px}
</style>
</head>
<body>
<main class="poster">
  <svg class="scene" viewBox="0 0 800 1200" preserveAspectRatio="none" aria-hidden="true">
    <defs>
      <linearGradient id="skyGrad" x1="0" y1="0" x2="0" y2="1">
        <stop offset="0" stop-color="#67B69A"/>
        <stop offset="0.22" stop-color="#5DA67C"/>
        <stop offset="0.34" stop-color="#3F7D3E"/>
        <stop offset="0.42" stop-color="#356E37"/>
        <stop offset="1" stop-color="#5F8E34"/>
      </linearGradient>
      <linearGradient id="illustrationGrad" x1="0" y1="0" x2="0" y2="1">
        <stop offset="0" stop-color="#2F6A3A"/>
        <stop offset="0.12" stop-color="#3A8F82"/>
        <stop offset="0.42" stop-color="#3A9486"/>
        <stop offset="0.52" stop-color="#5E9A3E"/>
        <stop offset="1" stop-color="#6E9B38"/>
      </linearGradient>
    </defs>
    <rect width="800" height="1200" fill="url(#skyGrad)"/>
  </svg>

  <svg class="scene" viewBox="0 0 800 1200" preserveAspectRatio="none" role="img" aria-label="Retro illustration of a lakeside campground: pine forest, lake with a dock, a silver travel trailer, two kids playing disc golf and a dog on a grassy path">
    <rect x="0" y="392" width="800" height="808" fill="url(#illustrationGrad)"/>
  </svg>

  <div class="brand"><span class="brand-mark"></span><span>BRIGHTPINE<br>RESORT</span></div>

  <svg class="badge" viewBox="0 0 218 202" aria-hidden="true">
    <ellipse cx="109" cy="101" rx="104" ry="96" fill="var(--cream)" stroke="#9A8F78" stroke-width="5"/>
  </svg>
  <div class="badge-text">LIMITED<br>SITES<br>AVAILABLE</div>

  <h1 class="headline epic">EPIC</h1>
  <h1 class="headline camp">CAMPGROUND</h1>
  <p class="subhead l1">AWAIT AT CEDAR HOLLOW</p>
  <p class="subhead l2">RESORT &amp; MARINA</p>
  <p class="tagline">YOUR NORTH TOLVIN LAKE ADVENTURE!</p>

  <p class="offer l1">WE PROVIDE SEASONAL <span class="hl">FULL SERVICE SITE</span></p>
  <p class="offer l2"><span class="hl">WITH</span> MARINA AND LAKE ACCESS</p>

  <h2 class="amenities-title">AVAILABLE:</h2>
  <section class="amenities">
    <ul class="amenity-list">
      <li>SAUNA/PLUNGE</li>
      <li>DISC GOLF</li>
      <li>HIKING/QUAD TRAILS</li>
      <li>PET FRIENDLY</li>
    </ul>
  </section>

  <p class="referral">REFER A FRIEND &amp; GET A DISCOUNT!</p>

  <div class="contact">
    <span>Contact us :</span>
    <span class="phone">
      <svg width="22" height="22" viewBox="0 0 24 24" aria-hidden="true"><path d="M6.6 10.8a15 15 0 0 0 6.6 6.6l2.2-2.2a1 1 0 0 1 1-.25 11.4 11.4 0 0 0 3.6.57 1 1 0 0 1 1 1V20a1 1 0 0 1-1 1A17 17 0 0 1 3 4a1 1 0 0 1 1-1h3.5a1 1 0 0 1 1 1c0 1.25.2 2.45.57 3.6a1 1 0 0 1-.25 1z" fill="none" stroke="var(--cream)" stroke-width="1.8"/></svg>
      + 44 (123) 98 76 543
    </span>
  </div>
</main>
</body>
</html>
```